Tessel PR (young, fun PR agency) needs a Business Card Design

We need a new business card design that reflects who we are as a company. We're a Sydney-based PR agency that's six years old with clients including Blue Heron, Duneprint, OLVEN, Lou Carvell etc. - just check out our website for more info: www.tesselpr.com.au. We would like to see designs that bring to life our company name and what we do (generating media coverage for brands on TV, radio, online and in newspapers and magazines). We don't want a corporate style card but one that people take notice of and think 'wow that's a cool business card'. It doesn't have to be the standard rectangle shape and can incorporate humour.

Target Market(s)

Clients (generally cool/creative types) and media

Industry/Entity Type

Business

Requirements
Must have
• The card must feature our business logo (which can be updated if you like) and use both sides.
Nice to have
• The card could feature a cool illustration

```html
<!DOCTYPE html>
<html lang="en">
<head>
<meta charset="utf-8">
<title>Tessel PR – Business Card</title>
<link rel="stylesheet" href="https://fonts.googleapis.com/css2?family=Quicksand:wght@500;700&display=swap">
<style>
  :root {
    --page-bg: #ece6e1;
    --card-light: #ffffff;
    --card-mid: #e6e6e6;
    --card-edge: #bdbdbd;
    --ink: #1a1a1a;
    --ink-soft: #2b2b2b;
    --accent: #f7a64a;
    --figure-light: #eeeeee;
    --figure-dark: #a9a9a9;
  }
  * { margin: 0; padding: 0; box-sizing: border-box; }
  html, body {
    width: 1003px; height: 1200px; overflow: hidden;
    background: var(--page-bg);
    font-family: "Quicksand", sans-serif;
    color: var(--ink);
  }
  .canvas { position: relative; width: 1003px; height: 1200px; }

  .card {
    position: absolute; left: 118px; width: 762px; height: 495px;
    border-radius: 22px 70px 22px 70px;
    background: radial-gradient(ellipse at 50% 55%, var(--card-light) 0%, var(--card-mid) 45%, var(--card-edge) 100%);
    box-shadow: 3px 4px 8px rgba(0,0,0,0.45);
    overflow: hidden;
  }
  .card--front { top: 64px; }
  .card--back { top: 639px; }

  .target-ring { position: absolute; left: 558px; top: 43px; width: 160px; height: 160px; }

  .brand {
    position: absolute; left: 40px; top: 250px;
    transform-origin: 0 0; transform: rotate(-18deg);
  }
  .brand__name {
    position: absolute; left: 22px; top: -92px; white-space: nowrap;
    font-family: "Quicksand", sans-serif; font-weight: 700;
    font-size: 86px; line-height: 1; letter-spacing: 1px;
    text-transform: uppercase; color: var(--ink);
  }
  .brand__band {
    position: absolute; left: 0; top: 0; width: 668px; height: 38px;
    background: var(--accent);
  }
  .brand__tagline {
    position: absolute; left: 16px; top: 4px; white-space: nowrap;
    font-weight: 700; font-size: 25px; line-height: 30px;
    letter-spacing: 0.5px; text-transform: uppercase; color: var(--ink);
  }

  .people-illustration {
    position: absolute; left: 491px; top: 240px; width: 228px; height: 172px;
    border-radius: 50%;
    background: radial-gradient(ellipse at 50% 50%, var(--figure-light) 0%, #d0d0d0 55%, rgba(189,189,189,0) 75%);
  }

  .address {
    position: absolute; right: 62px; top: 446px;
    font-weight: 500; font-size: 22px; color: var(--ink-soft); white-space: nowrap;
  }

  .contact { position: absolute; right: 44px; text-align: right; white-space: nowrap; color: var(--ink-soft); }
  .contact__name { top: 262px; font-size: 29px; font-weight: 500; }
  .contact__role { top: 305px; font-size: 20px; font-weight: 500; }
  .contact__phone { top: 410px; font-size: 21px; font-weight: 500; }
  .contact__email { top: 444px; font-size: 21px; font-weight: 500; }
</style>
</head>
<body>
<main class="canvas">

  <section class="card card--front" aria-label="Card front">
    <svg class="target-ring" viewBox="0 0 160 160" aria-hidden="true">
      <circle cx="80" cy="80" r="70" fill="none" stroke="#1a1a1a" stroke-width="9"/>
    </svg>
    <div class="brand">
      <div class="brand__name">Tessel PR</div>
      <div class="brand__band"><span class="brand__tagline">Public Relations</span></div>
    </div>
    <div class="people-illustration" role="img" aria-label="Illustration of grey 3D figures standing around a target circle"></div>
    <p class="address">Level 3, 48 Harlow Lane, Fernbrook, Sydney 2011</p>
  </section>

  <section class="card card--back" aria-label="Card back">
    <svg class="target-ring" viewBox="0 0 160 160" aria-hidden="true">
      <circle cx="80" cy="80" r="70" fill="none" stroke="#1a1a1a" stroke-width="9"/>
    </svg>
    <div class="brand">
      <div class="brand__name">Tessel PR</div>
      <div class="brand__band"><span class="brand__tagline">Public Relations</span></div>
    </div>
    <p class="contact contact__name">Nadia Whitcombe</p>
    <p class="contact contact__role">Managing Director</p>
    <p class="contact contact__phone">phone: 02 9480 1736</p>
    <p class="contact contact__email">nadia@tesselpr.com.au</p>
  </section>

</main>
</body>
</html>
```